We are needing a bookcover for a reprint of our book "Whispers Beneath the Amber Horizon". It takes a look at the geologic formation found in the great plains. Our original cover was colorful and showed rock layers. Something similar but different and eye catching would be great. a geologic cross section showing various layers or possibly some different rocks/soils. We are really open to suggestions attached is the current book cover with the colored layers and the cover from the 80s.

Target Market(s)

Adult Readers

Industry/Entity Type

Nonprofit retail - science - nature

Requirements
Must have
• Geology or rock layers
Nice to have
• Books title, Geologic cross section
Should not have
• People or animals, no photos prefer sketch

```html
<!DOCTYPE html>
<html lang="en">
<head>
<meta charset="utf-8">
<title>Whispers Beneath the Amber Horizon — Cover</title>
<link rel="stylesheet" href="https://fonts.googleapis.com/css2?family=Roboto+Slab:wght@700;800&display=swap">
<style>
  :root {
    --backdrop: #d3d4d6;
    --sand: #fee1b4;
    --ink: #111111;
    --label: #ffffff;
    --snow: #fcf5f6;
    --amber: #fdb608;
    --leaf: #7ad900;
    --green: #37db00;
    --navy: #0019b0;
    --royal: #0a00c8;
    --umber: #996300;
    --earth: #512100;
  }
  * { box-sizing: border-box; margin: 0; padding: 0; }
  html, body {
    width: 1200px; height: 1028px; overflow: hidden;
    background: var(--backdrop);
  }
  .cover {
    position: absolute;
    left: 270px; top: 51px;
    width: 660px; height: 925px;
    background: var(--sand);
    overflow: hidden;
  }
  .strata-art {
    position: absolute;
    left: 0; right: 0; top: 300px; bottom: 0;
    background: linear-gradient(
      to bottom,
      var(--sand) 0%,
      var(--snow) 8%,
      var(--leaf) 20%,
      var(--navy) 30%,
      var(--green) 42%,
      var(--royal) 55%,
      var(--snow) 68%,
      var(--sand) 78%,
      var(--amber) 85%,
      var(--umber) 92%,
      var(--earth) 100%
    );
  }
  .title {
    position: absolute; left: 0; right: 0; top: 68px;
    text-align: center;
    font-family: "Roboto Slab", "Rockwell", serif;
    color: var(--ink);
  }
  .title-kicker {
    display: inline-block;
    background: var(--label);
    font-weight: 800;
    font-size: 28px;
    letter-spacing: 2px;
    line-height: 47px;
    padding: 0 8px;
    text-transform: uppercase;
  }
  .title-main {
    display: block;
    margin: 34px auto 0;
    width: fit-content;
    background: var(--label);
    font-weight: 700;
    font-size: 76px;
    line-height: 85px;
    letter-spacing: -1px;
    padding: 0 12px;
  }
</style>
</head>
<body>
  <main class="cover">
    <div class="strata-art" role="img" aria-label="Illustration of colourful wavy rock strata and ridges in blues, greens, amber and earth browns"></div>
    <h1 class="title">
      <span class="title-kicker">Whispers Beneath the</span>
      <span class="title-main">Amber Horizon</span>
    </h1>
  </main>
</body>
</html>
```